Business Card for Consulting Company

I would need a business card for my consulting company - the company brand and logos are defined and shared as part of this project. The proposed design for the business card can be reused as inspiration for my email signature.

```html
<!DOCTYPE html>
<html lang="en">
<head>
<meta charset="utf-8">
<title>Halvern Partners – Business Card</title>
<link rel="stylesheet" href="https://fonts.googleapis.com/css2?family=Questrial&family=Roboto:wght@400&display=swap">
<style>
  :root {
    --page-bg: #ffffff;
    --card-front-bg: #e6e6e6;
    --brand-teal: #02aaaa;
    --ink-dark: #3d3d3d;
    --ink-light: #ffffff;
  }
  * { box-sizing: border-box; margin: 0; padding: 0; }
  html, body {
    width: 1093px;
    height: 1200px;
    overflow: hidden;
    background: var(--page-bg);
  }
  .canvas {
    position: relative;
    width: 1093px;
    height: 1200px;
  }
  .card {
    position: absolute;
    left: 265px;
    width: 580px;
    height: 357px;
  }
  .card--front {
    top: 226px;
    background: var(--card-front-bg);
  }
  .card--back {
    top: 620px;
    background: var(--brand-teal);
  }

  .wordmark {
    position: absolute;
    left: 0;
    right: 0;
    display: flex;
    align-items: center;
    justify-content: center;
    gap: 12px;
    font-family: "Questrial", sans-serif;
    font-weight: 400;
    white-space: nowrap;
  }
  .wordmark__dot {
    border-radius: 50%;
    flex: none;
  }
  .card--front .wordmark {
    top: 62px;
    font-size: 34px;
    color: var(--brand-teal);
  }
  .card--front .wordmark__dot {
    width: 22px;
    height: 22px;
    background: var(--brand-teal);
  }
  .card--back .wordmark {
    top: 145px;
    font-size: 44px;
    color: var(--ink-light);
  }
  .card--back .wordmark__dot {
    width: 28px;
    height: 28px;
    background: var(--ink-light);
  }

  .identity {
    position: absolute;
    top: 186px;
    left: 0;
    right: 0;
    text-align: center;
  }
  .identity__name {
    font-family: "Questrial", sans-serif;
    font-size: 21px;
    letter-spacing: 2px;
    color: var(--ink-dark);
    line-height: 1.2;
  }
  .identity__surname { color: var(--brand-teal); }
  .identity__role {
    margin-top: 6px;
    font-family: "Roboto", sans-serif;
    font-size: 14px;
    letter-spacing: 1.6px;
    color: var(--ink-dark);
  }
  .identity__rule {
    width: 73px;
    height: 1px;
    margin: 10px auto 0;
    background: var(--brand-teal);
    border: 0;
  }

  .contact {
    position: absolute;
    top: 254px;
    left: 0;
    right: 0;
    text-align: center;
    font-family: "Roboto", sans-serif;
    color: var(--ink-dark);
    list-style: none;
  }
  .contact__item {
    font-size: 14px;
    letter-spacing: 1.5px;
    line-height: 22px;
  }
  .contact__item--phone {
    font-size: 16px;
    letter-spacing: 1.4px;
  }
</style>
</head>
<body>
<main class="canvas">
  <section class="card card--front" aria-label="Business card front">
    <div class="wordmark">
      <span class="wordmark__dot" aria-hidden="true"></span>
      <span class="wordmark__name">Halvern Partners</span>
    </div>

    <div class="identity">
      <p class="identity__name">MAREN <span class="identity__surname">HOLLOWAY</span></p>
      <p class="identity__role">FOUNDER &amp; CEO</p>
      <hr class="identity__rule">
    </div>

    <ul class="contact">
      <li class="contact__item contact__item--phone">044-987 654 321</li>
      <li class="contact__item">INFO@HALVERNPARTNERS.COM</li>
      <li class="contact__item">WWW.HALVERNPARTNERS.COM</li>
    </ul>
  </section>

  <section class="card card--back" aria-label="Business card back">
    <div class="wordmark">
      <span class="wordmark__dot" aria-hidden="true"></span>
      <span class="wordmark__name">Halvern Partners</span>
    </div>
  </section>
</main>
</body>
</html>
```